Poster Design For Obstacle Run

Design a poster for the Copper Dune Obstacle run.
Text: Copper Dune Obstacle Run. May 12th, 2018. Sittard. www.copperdunerun.nl. I have added a lot of pictures.
Furthermore, the logo should be included. As an example I included a poster from the valkor race that we really like (valkor team challenge) and also. Feel free to take a look at our website for inspiration: www.copperdunerun.nl

```html
<!DOCTYPE html>
<html lang="en">
<head>
<meta charset="utf-8">
<title>Copper Dune Obstacle Run — May 12th, 2018, Sittard</title>
<link rel="stylesheet" href="https://fonts.googleapis.com/css2?family=Alfa+Slab+One&family=Montserrat:wght@500&display=swap">
<style>
  :root {
    --rust: #b0502a;
    --white: #ffffff;
    --band: rgba(176, 80, 42, 0.72);
    --wall-dark: #6f6c68;
    --wall-mid: #9d9993;
    --wall-light: #cfc9c1;
    --mud-dark: #4a3a30;
    --mud-mid: #7a6352;
    --mud-light: #a48a74;
    --shirt: #d8692a;
    --shirt-dark: #a94a1c;
    --foliage: #6b7d55;
  }
  html, body {
    margin: 0;
    padding: 0;
    overflow: hidden;
    background: #ffffff;
  }
  .poster {
    position: relative;
    width: 1200px;
    height: 926px;
    overflow: hidden;
  }
  .poster__photo {
    position: absolute;
    inset: 0;
    background:
      radial-gradient(ellipse 260px 330px at 1050px 250px, var(--shirt) 0%, var(--shirt-dark) 55%, transparent 80%),
      radial-gradient(ellipse 150px 200px at 880px 60px, var(--mud-light) 0%, transparent 75%),
      radial-gradient(ellipse 120px 160px at 830px 160px, var(--foliage) 0%, transparent 80%),
      radial-gradient(ellipse 420px 190px at 720px 640px, var(--mud-mid) 0%, var(--mud-dark) 50%, transparent 85%),
      radial-gradient(ellipse 300px 170px at 400px 420px, var(--mud-light) 0%, var(--mud-mid) 45%, transparent 85%),
      radial-gradient(ellipse 220px 200px at 1080px 720px, var(--mud-dark) 0%, transparent 80%),
      linear-gradient(155deg, var(--wall-mid) 0%, var(--wall-light) 30%, var(--wall-mid) 55%, var(--wall-light) 75%, var(--wall-dark) 100%);
  }
  .poster__title,
  .poster__details {
    position: absolute;
    left: 38px;
    margin: 0;
    font-family: "Alfa Slab One", "Rockwell Extra Bold", serif;
    font-weight: 400;
    color: var(--rust);
    text-transform: uppercase;
    text-shadow:
      -3px -3px 0 var(--white), 3px -3px 0 var(--white),
      -3px 3px 0 var(--white), 3px 3px 0 var(--white),
      0 -3px 0 var(--white), 0 3px 0 var(--white),
      -3px 0 0 var(--white), 3px 0 0 var(--white);
  }
  .poster__title {
    top: 86px;
    font-size: 87px;
    line-height: 96px;
    letter-spacing: 5px;
  }
  .poster__details {
    top: 346px;
    font-size: 61px;
    line-height: 82px;
    letter-spacing: 6px;
  }
  .poster__details sup {
    font-size: 0.5em;
    vertical-align: 0.85em;
    line-height: 0;
    letter-spacing: 2px;
  }
  .poster__web-band {
    position: absolute;
    left: 0;
    top: 845px;
    width: 1200px;
    height: 56px;
    background: var(--band);
    display: flex;
    align-items: center;
    justify-content: center;
  }
  .poster__url {
    font-family: "Montserrat", sans-serif;
    font-weight: 500;
    font-size: 30px;
    letter-spacing: 2.5px;
    color: var(--white);
    text-transform: uppercase;
  }
</style>
</head>
<body>
  <main class="poster">
    <div class="poster__photo" role="img" aria-label="Close-up action photo of a mud-covered runner in an orange shirt climbing a rope up a corrugated wall"></div>
    <h1 class="poster__title">Copper Dune<br>Obstacle Run</h1>
    <p class="poster__details">May 12<sup>th</sup>, 2018<br>Sittard</p>
    <div class="poster__web-band">
      <span class="poster__url">www.copperdunerun.nl</span>
    </div>
  </main>
</body>
</html>
```